Chinese New Year Party

To create an invitation for a party.

Invitation to be sent by email.
Party date : Feb 1 2014
RSVP : 22 Jan 2014 to lena@pinecourtyard.net or tomas@pinecourtyard.net
address 17 Copperfield Walk, Singapore 468215
(add google map address)

Message : "We'd love you to join us as we celebrate Chinese New Year 2014 with some great music, some horses doeuvres, exotic cocktails, and top company.
We'll horse around a little as well ;)
Tomas & Lena"

Theme of the invite should be Chinese/Oriental
Images should include a horse ( for the Chinese new year ) with the number 69 on the horse. Other images should include a DJ with music decks and images of cocktails.

Target Market(s)

Target market 30-40 year olds who enjoy nite clubs

```html
<!DOCTYPE html>
<html lang="en">
<head>
<meta charset="utf-8">
<title>Chinese New Year Party Invitation</title>
<link rel="stylesheet" href="https://fonts.googleapis.com/css2?family=Almendra+SC&family=LXGW+WenKai+TC&display=swap">
<style>
  :root {
    --maroon-deep: #2e0404;
    --maroon: #5c0a0c;
    --red: #b3121a;
    --red-bright: #d8202a;
    --band-red: #c4141d;
    --band-red-dark: #7d0b10;
    --gold: #c99a3a;
    --gold-dark: #6e4a14;
    --cream: #fff6ea;
    --label: #4a0608;
  }
  html, body {
    margin: 0;
    padding: 0;
    overflow: hidden;
    background: #ffffff;
  }
  .invitation {
    position: relative;
    width: 1200px;
    height: 545px;
    overflow: hidden;
    background: radial-gradient(ellipse at 95% 30%, var(--red-bright) 0%, var(--red) 30%, var(--maroon) 70%, var(--maroon-deep) 100%);
    font-family: "Almendra SC", Georgia, serif;
  }
  .greeting {
    position: absolute;
    left: 415px;
    top: 6px;
    margin: 0;
    font-family: "LXGW WenKai TC", "Noto Serif TC", serif;
    font-weight: 400;
    font-size: 84px;
    line-height: 1;
    letter-spacing: 2px;
    color: var(--cream);
  }
  .band {
    position: absolute;
    left: 0;
    top: 130px;
    width: 1200px;
    height: 282px;
    background: linear-gradient(90deg, var(--band-red-dark) 0%, var(--band-red) 35%, var(--red-bright) 100%);
  }
  .band-trim {
    position: absolute;
    left: 0;
    width: 1200px;
    height: 18px;
    background: linear-gradient(180deg, var(--gold-dark) 0%, var(--gold) 50%, var(--gold-dark) 100%);
    opacity: 0.85;
  }
  .band-trim--top { top: 128px; }
  .band-trim--bottom { top: 392px; }
  .horse-art {
    position: absolute;
    left: 0;
    top: 70px;
    width: 370px;
    height: 475px;
    background: radial-gradient(ellipse at 45% 45%, rgba(255,246,234,0.16) 0%, rgba(255,246,234,0.06) 55%, rgba(255,246,234,0) 75%);
  }
  .details {
    position: absolute;
    left: 368px;
    top: 156px;
    margin: 0;
    list-style: none;
    padding: 0;
    font-size: 21px;
    line-height: 30.5px;
    color: var(--cream);
  }
  .details .label { color: var(--label); }
  .message {
    position: absolute;
    left: 470px;
    top: 292px;
    width: 715px;
    margin: 0;
    text-align: center;
    font-size: 18px;
    line-height: 21px;
    color: var(--cream);
  }
</style>
</head>
<body>
  <main class="invitation">
    <div class="band"></div>
    <div class="band-trim band-trim--top" role="img" aria-label="Gold Chinese key-pattern border"></div>
    <div class="band-trim band-trim--bottom" role="img" aria-label="Gold Chinese key-pattern border"></div>

    <h1 class="greeting" lang="zh-Hant">中國新年快樂</h1>

    <div class="horse-art" role="img" aria-label="White brush-stroke drawing of a horse's head with the number 69 on its neck"></div>

    <ul class="details">
      <li><span class="label">Party Date :</span> February 1, 2014</li>
      <li><span class="label">RSVP :</span> January 22, 2014 to: lena@pinecourtyard.net or</li>
      <li>tomas@pinecourtyard.net</li>
      <li><span class="label">Address:</span> 17 Copperfield Walk, Singapore 468215</li>
    </ul>

    <p class="message">
      We'd love you to join us as we celebrate Chinese New Year<br>
      2014 with some great music, some horses doeuvres, exotic<br>
      cocktails, and top company.<br>
      We'll horse around a little as well ;)
    </p>
  </main>
</body>
</html>
```